Garnett and Lyle Personal Injury Billboard

We'd like a clean/modern billboard to build brand awareness for our law firm in the area of personal injury. Ideally, we like the word "Injured?" or something similar in large lettering.

I'm attaching images, logo and award badges which could be used. The billboards will be 14x48 ft and 10.6x36.

We are open to different color ideas, fonts, and artwork. Creative but not too busy with wording. Our web page is www.kgarnettfirm.example

Garnett & Lyle Law Firm
(555) 318-4092

```html
<!DOCTYPE html>
<html lang="en">
<head>
<meta charset="utf-8">
<title>Garnett &amp; Lyle Personal Injury Billboard</title>
<link rel="stylesheet" href="https://fonts.googleapis.com/css2?family=Montserrat:wght@600;700;800;900&display=swap">
<style>
  :root {
    --canvas: #d3d4d7;
    --navy: #0b1a33;
    --navy-deep: #07111f;
    --blue: #1f74ea;
    --blue-soft: #2b5fa8;
    --white: #ffffff;
    --ink: #13233f;
    --label: #3b3d42;
    --photo-a: #8a8f98;
    --photo-b: #4d5360;
    --badge: #2f3b52;
  }
  * { box-sizing: border-box; margin: 0; padding: 0; }
  html, body { width: 764px; height: 1200px; overflow: hidden; }
  body {
    background: var(--canvas);
    position: relative;
    font-family: "Montserrat", Arial, sans-serif;
  }
  .billboard {
    position: absolute;
    width: 48em;
    height: 14em;
    overflow: hidden;
    background:
      linear-gradient(115deg, transparent 52%, rgba(31,116,234,.18) 52%, rgba(31,116,234,.18) 60%, transparent 60%),
      linear-gradient(100deg, var(--navy-deep) 0%, var(--navy) 55%, #10264a 100%);
    box-shadow: 0 .2em .6em rgba(0,0,0,.25);
  }
  .billboard--hero   { font-size: 14.25px; left: 40px;  top: 170px; }
  .billboard--large  { font-size: 12.96px; left: 71px;  top: 700px; }
  .billboard--small  { font-size: 10.42px; left: 132px; top: 960px; }

  /* every positioned box sits at base size; the text inside carries the scale */
  .brand {
    position: absolute; left: 1.2em; top: 1em;
    display: flex; align-items: center; gap: .6em;
  }
  .brand__mark { width: 1.1em; height: 1.1em; background: var(--blue); flex: none; }
  .brand__name {
    color: var(--white); font-weight: 800; font-size: 1.35em;
    line-height: 1.05; letter-spacing: .02em; width: 6.4em;
  }
  .attorneys {
    position: absolute; left: 1.2em; top: 4.6em;
    width: 11.6em; height: 9.4em;
    border-radius: .3em .3em 0 0;
    background: linear-gradient(180deg, var(--photo-a), var(--photo-b));
  }
  .divider {
    position: absolute; left: 13.8em; top: 1em; width: .12em; height: 12em;
    background: var(--blue-soft);
  }
  .headline {
    position: absolute; left: 15em; top: .6em; width: 32em;
    margin: 0;
    font-size: 1em;
  }
  .headline__text {
    display: block;
    font-family: "Montserrat", Arial, sans-serif; font-weight: 900;
    font-size: 5.3em; line-height: 1; color: var(--blue);
    letter-spacing: -.01em; white-space: nowrap;
  }
  .phone {
    position: absolute; left: 15.6em; top: 6.6em;
    display: flex; align-items: center; gap: .8em;
  }
  .phone__icon { width: 2em; height: 2em; flex: none; }
  .phone__number {
    color: var(--white); font-weight: 700; font-size: 2.5em;
    line-height: 1; white-space: nowrap; letter-spacing: .01em;
  }
  .web-band {
    position: absolute; left: 14.4em; top: 10.6em; width: 26.6em; height: 2.6em;
    background: var(--white);
    display: flex; align-items: center; justify-content: center;
  }
  .web-band__url {
    color: var(--ink); font-weight: 700; font-size: 1.65em;
    letter-spacing: .01em; white-space: nowrap;
  }
  .award {
    position: absolute; left: 42.2em; top: 8.4em; width: 4.4em; height: 4.4em;
    background: var(--badge); border: .15em solid var(--white);
  }
  .size-label {
    position: absolute; width: 764px; text-align: center;
    font-family: "Montserrat", Arial, sans-serif; font-weight: 600;
    font-size: 18px; color: var(--label); letter-spacing: .04em;
  }
  .size-label--large { top: 898px; }
  .size-label--small { top: 1125px; }
</style>
</head>
<body>

  <section class="billboard billboard--hero" aria-label="Billboard design">
    <div class="brand"><span class="brand__mark"></span><span class="brand__name">GARNETT &amp; LYLE</span></div>
    <div class="attorneys" role="img" aria-label="Portrait of the firm's two attorneys in suits"></div>
    <div class="divider"></div>
    <h1 class="headline"><span class="headline__text">INJURED?</span></h1>
    <div class="phone">
      <svg class="phone__icon" viewBox="0 0 24 24" aria-hidden="true"><circle cx="12" cy="12" r="12" fill="#1f74ea"/><path d="M8.2 5.5l2 .2 1 3-1.4 1.1a8 8 0 0 0 4.4 4.4l1.1-1.4 3 1 .2 2c-.1 1-1 1.7-2 1.7A11 11 0 0 1 6.5 7.5c0-1 .7-1.9 1.7-2z" fill="#fff"/></svg>
      <span class="phone__number">(555) 318-4092</span>
    </div>
    <div class="web-band"><span class="web-band__url">www.kgarnettfirm.example</span></div>
    <div class="award" role="img" aria-label="Award badge"></div>
  </section>

  <section class="billboard billboard--large" aria-label="Billboard design, 48 by 14 feet">
    <div class="brand"><span class="brand__mark"></span><span class="brand__name">GARNETT &amp; LYLE</span></div>
    <div class="attorneys" role="img" aria-label="Portrait of the firm's two attorneys in suits"></div>
    <div class="divider"></div>
    <div class="headline"><span class="headline__text">INJURED?</span></div>
    <div class="phone">
      <svg class="phone__icon" viewBox="0 0 24 24" aria-hidden="true"><circle cx="12" cy="12" r="12" fill="#1f74ea"/><path d="M8.2 5.5l2 .2 1 3-1.4 1.1a8 8 0 0 0 4.4 4.4l1.1-1.4 3 1 .2 2c-.1 1-1 1.7-2 1.7A11 11 0 0 1 6.5 7.5c0-1 .7-1.9 1.7-2z" fill="#fff"/></svg>
      <span class="phone__number">(555) 318-4092</span>
    </div>
    <div class="web-band"><span class="web-band__url">www.kgarnettfirm.example</span></div>
    <div class="award" role="img" aria-label="Award badge"></div>
  </section>
  <p class="size-label size-label--large">48 X 14</p>

  <section class="billboard billboard--small" aria-label="Billboard design, 36 by 10.6 feet">
    <div class="brand"><span class="brand__mark"></span><span class="brand__name">GARNETT &amp; LYLE</span></div>
    <div class="attorneys" role="img" aria-label="Portrait of the firm's two attorneys in suits"></div>
    <div class="divider"></div>
    <div class="headline"><span class="headline__text">INJURED?</span></div>
    <div class="phone">
      <svg class="phone__icon" viewBox="0 0 24 24" aria-hidden="true"><circle cx="12" cy="12" r="12" fill="#1f74ea"/><path d="M8.2 5.5l2 .2 1 3-1.4 1.1a8 8 0 0 0 4.4 4.4l1.1-1.4 3 1 .2 2c-.1 1-1 1.7-2 1.7A11 11 0 0 1 6.5 7.5c0-1 .7-1.9 1.7-2z" fill="#fff"/></svg>
      <span class="phone__number">(555) 318-4092</span>
    </div>
    <div class="web-band"><span class="web-band__url">www.kgarnettfirm.example</span></div>
    <div class="award" role="img" aria-label="Award badge"></div>
  </section>
  <p class="size-label size-label--small">36 X 10.6</p>

</body>
</html>
```